Double-sided Business card design needed

I work as an independent consultant in a range of fields, and I need a business card to describes the two main business operations in a two-sided format:

(1) KILT - Kinship Inclusion Learning Therapy

(2) PORT - Promoting Original Regional Tribes

My personal profile so far has been describing myself as:
Dr Gavin Thorpe- Independent R&D Consultant in Community Wellbeing, Education, Mental Health and Disability Support Reform

Industry/Entity Type

Business

Contact Information for Business Card

I need a double-sided business card, describing two different but related businesses that I operate: one in Disability & Mental Health, Education and Community Wellbeing consulting, teaching and research; the other in Indigenous/First Nations-specific community cultural development

Logo Text

See the two business names below for logo text - and they need two different logo designs

Logo styles of interest
Pictorial/Combination Logo

```html
<!DOCTYPE html>
<html lang="en">
<head>
<meta charset="utf-8">
<title>Dr Gavin Thorpe — KILT &amp; PORT Business Cards</title>
<link rel="stylesheet" href="https://fonts.googleapis.com/css2?family=Questrial&family=Tinos&display=swap">
<style>
  :root {
    --page-bg: #d9d6d2;
    --card-top: #5e5e5e;
    --card-bottom: #3f3f3f;
    --crimson: #c8203a;
    --amber: #d9781f;
    --ink-light: #f2f2f2;
    --panel-dark: #262626;
  }
  * { margin: 0; padding: 0; box-sizing: border-box; }
  html, body { width: 1200px; height: 1021px; overflow: hidden; }
  body {
    background: var(--page-bg);
    font-family: "Questrial", sans-serif;
    position: relative;
  }
  .card {
    position: absolute;
    top: 165px;
    width: 480px;
    height: 690px;
    border-radius: 4px;
    background:
      radial-gradient(ellipse 70% 45% at 50% 22%, rgba(255,255,255,0.14), transparent 70%),
      linear-gradient(180deg, var(--card-top), var(--card-bottom));
    box-shadow: 0 14px 30px rgba(0,0,0,0.35);
    overflow: hidden;
  }
  .card--kilt { left: 90px; }
  .card--port { left: 630px; }

  .brand-mark {
    position: absolute;
    left: 0; right: 0;
    top: 70px;
    display: flex;
    align-items: center;
    justify-content: center;
    gap: 14px;
  }
  .brand-mark__dot {
    width: 26px; height: 26px; border-radius: 50%;
    background: var(--amber);
  }
  .brand-mark__name {
    font-size: 58px;
    color: var(--crimson);
    letter-spacing: 6px;
  }
  .brand-glow {
    position: absolute;
    left: 190px; top: 190px;
    width: 100px; height: 10px;
    border-radius: 50%;
    background: radial-gradient(ellipse, rgba(255,255,255,0.5), transparent 70%);
  }

  .map-area {
    position: absolute;
    left: 100px; top: 28px;
    width: 280px; height: 190px;
    border-radius: 6px;
    background: linear-gradient(180deg, #2e2e2e, var(--panel-dark));
  }
  .card--port .brand-mark { top: 88px; }

  .person {
    position: absolute;
    left: 38px;
  }
  .card--kilt .person { top: 215px; }
  .card--port .person { top: 240px; }
  .person__name {
    position: relative;
    padding-left: 32px;
    font-size: 25px;
    font-weight: 400;
    color: var(--crimson);
    letter-spacing: 1px;
    text-transform: uppercase;
  }
  .person__name::before {
    content: "";
    position: absolute;
    left: 0; top: 3px;
    width: 7px; height: 28px;
    background: var(--amber);
  }
  .person__roles {
    list-style: none;
    margin-top: 4px;
    padding-left: 24px;
    color: var(--ink-light);
    font-size: 19px;
    line-height: 25px;
  }

  .contact {
    position: absolute;
    left: 88px;
    list-style: none;
    color: var(--ink-light);
    font-size: 20px;
    line-height: 26px;
  }
  .card--kilt .contact { top: 345px; }
  .card--port .contact { top: 368px; }
  .contact li { display: flex; align-items: flex-start; gap: 8px; }
  .contact svg { flex: none; margin-top: 5px; }

  .acronym-line {
    position: absolute;
    left: 30px;
    font-size: 29px;
    line-height: 40px;
    color: var(--amber);
  }
  .card--kilt .acronym-line { top: 470px; }
  .card--port .acronym-line { top: 485px; }
  .acronym-line b { font-weight: 400; color: var(--crimson); }

  .acronym-big {
    position: absolute;
    left: 20px;
    font-family: "Tinos", serif;
    font-size: 108px;
    line-height: 1;
    color: var(--crimson);
    letter-spacing: -2px;
  }
  .card--kilt .acronym-big { top: 560px; }
  .card--port .acronym-big { top: 570px; }
</style>
</head>
<body>

  <section class="card card--kilt" aria-label="KILT business card">
    <div class="brand-mark">
      <span class="brand-mark__dot"></span>
      <span class="brand-mark__name">KILT</span>
    </div>
    <div class="brand-glow"></div>

    <div class="person">
      <h1 class="person__name">Dr . Gavin Thorpe</h1>
      <ul class="person__roles">
        <li>Education</li>
        <li>Mental Health</li>
        <li>Disability Support Reform</li>
      </ul>
    </div>

    <ul class="contact">
      <li>
        <svg width="16" height="16" viewBox="0 0 16 16" aria-hidden="true"><path d="M4 1l3 3-2 2c1 2 3 4 5 5l2-2 3 3-2 3C7 15 1 9 1 3z" fill="none" stroke="#c8203a" stroke-width="1.5"/></svg>
        61-8-89270415
      </li>
      <li>
        <svg width="18" height="14" viewBox="0 0 18 14" aria-hidden="true"><rect x="0" y="1" width="18" height="12" rx="1" fill="#c8203a"/></svg>
        gavin.thorpe47@mailbox.net
      </li>
      <li>
        <svg width="14" height="18" viewBox="0 0 14 18" aria-hidden="true"><path d="M7 0a6 6 0 0 1 6 6c0 5-6 12-6 12S1 11 1 6a6 6 0 0 1 6-6z" fill="#c8203a"/><circle cx="7" cy="6" r="2" fill="#4a4a4a"/></svg>
        <span>14 Harlow St, Larrak Bay,<br>Darwin NT 0810</span>
      </li>
    </ul>

    <p class="acronym-line"><b>K</b>inship <b>I</b>nclusion<br><b>L</b>earning <b>T</b>herapy</p>
    <p class="acronym-big">K.I.L.T</p>
  </section>

  <section class="card card--port" aria-label="PORT business card">
    <div class="map-area" role="img" aria-label="Map illustration area behind the PORT name"></div>
    <div class="brand-mark">
      <span class="brand-mark__dot"></span>
      <span class="brand-mark__name">PORT</span>
    </div>

    <div class="person">
      <h2 class="person__name">Dr . Gavin Thorpe</h2>
      <ul class="person__roles">
        <li>Independent</li>
        <li>R &amp; D Consultant</li>
        <li>In Community Wellbeing</li>
      </ul>
    </div>

    <ul class="contact">
      <li>
        <svg width="16" height="16" viewBox="0 0 16 16" aria-hidden="true"><path d="M4 1l3 3-2 2c1 2 3 4 5 5l2-2 3 3-2 3C7 15 1 9 1 3z" fill="none" stroke="#c8203a" stroke-width="1.5"/></svg>
        0455 301 872
      </li>
      <li>
        <svg width="18" height="14" viewBox="0 0 18 14" aria-hidden="true"><rect x="0" y="1" width="18" height="12" rx="1" fill="#c8203a"/></svg>
        gavin.thorpe47@mailbox.net
      </li>
      <li>
        <svg width="14" height="18" viewBox="0 0 14 18" aria-hidden="true"><path d="M7 0a6 6 0 0 1 6 6c0 5-6 12-6 12S1 11 1 6a6 6 0 0 1 6-6z" fill="#c8203a"/><circle cx="7" cy="6" r="2" fill="#4a4a4a"/></svg>
        <span>58 Kellaway Rd,<br>Tarrin NSW 2450</span>
      </li>
    </ul>

    <p class="acronym-line"><b>P</b>romoting <b>O</b>riginal<br><b>R</b>egional <b>T</b>ribes</p>
    <p class="acronym-big">P.O.R.T</p>
  </section>

</body>
</html>
```